Harlow Ironworks Business Card

We need a business card design for a new small metal fabrication business in rural NSW, Australia.

The business (Harlow Ironworks) is owner operated by a man with the initials KB - much of the branding comes from this name.

Harlow Ironworks designs, engineers, repairs and manufactures a range of custom, quality metal works including vehicle trays, agricultural machinery impliments, trailers, wood splitters, fire pits, furniture etc.

The brand position focuses on custom work of the highest quality.

Business card design should show quality, attention to detail and stand out among a mass of business cards.

Logos are in the files

The grey color may be changed on the logo if required to stand out more.

There is an image attached of a simple card that is liked because it is clean, clear, simple, masculine and effective. It says 'quality'. As most of the work we do is custom it would be good to have the business card speak to this.

Target Market(s)

Rural and regional based Australians. Primarily adult male 25-60 yrs. Primary production / rural / travelling lifestyle.

Industry/Entity Type

Metal Fabrication

Contact Information for Business Card

The words 'custom quality fabrications' would be great somewhere perhaps on the backside (not on the information side)
Name
title
Phone: 0418 539 746 and (02) 6193 4827
email: info@harlowiw.com.au
www.harlowiw.com.au

address (2 lines)

Requirements
Nice to have
• Background colour should be very navy blue or black.
Should not have
• NO orange and blue combinations.
• Navy is OK

```html
<!DOCTYPE html>
<html lang="en">
<head>
<meta charset="utf-8">
<title>Harlow Ironworks – Business Card</title>
<link rel="stylesheet" href="https://fonts.googleapis.com/css2?family=Questrial&display=swap">
<style>
  :root {
    --backdrop: #2a2a2a;
    --card: #1c1c1c;
    --texture-tone: #242424;
    --brand-grey: #c9c9c9;
    --brand-green: #6cbf3f;
    --text-light: #f2f2f2;
    --text-muted: #cfcfcf;
    --divider: #8a8a8a;
  }
  * { margin: 0; padding: 0; box-sizing: border-box; }
  html, body {
    width: 1200px;
    height: 516px;
    overflow: hidden;
    background: var(--backdrop);
    font-family: "Questrial", "Century Gothic", sans-serif;
  }
  .canvas { position: relative; width: 1200px; height: 516px; }

  .card {
    position: absolute;
    top: 123px;
    width: 450px;
    height: 281px;
    background: var(--card);
    overflow: hidden;
    box-shadow: 0 4px 14px rgba(0,0,0,.35);
  }
  .card--front { left: 132px; }
  .card--back { left: 600px; width: 456px; }

  .texture-area {
    position: absolute;
    left: 0; top: 0;
    width: 100%; height: 249px;
    background: radial-gradient(ellipse at 60% 40%, var(--texture-tone) 0%, var(--card) 75%);
  }

  .brand {
    position: absolute;
    display: flex;
    align-items: center;
    color: var(--brand-grey);
    text-transform: uppercase;
    font-weight: 400;
  }
  .brand__square { background: var(--brand-grey); flex: none; }
  .brand__name { display: flex; flex-direction: column; line-height: 1; }

  .card--front .brand { left: 91px; top: 60px; gap: 12px; }
  .card--front .brand__square { width: 50px; height: 50px; }
  .card--front .brand__line--main { font-size: 38px; letter-spacing: 6px; }
  .card--front .brand__line--sub { font-size: 19px; letter-spacing: 7px; margin-top: 2px; }

  .card--back .brand { left: 93px; top: 106px; gap: 14px; }
  .card--back .brand__square { width: 55px; height: 55px; }
  .card--back .brand__line--main { font-size: 40px; letter-spacing: 6.5px; }
  .card--back .brand__line--sub { font-size: 20px; letter-spacing: 7.5px; margin-top: 2px; }

  .person {
    position: absolute;
    left: 120px; top: 141px;
    width: 200px;
    text-align: center;
  }
  .person__name { color: var(--brand-green); font-size: 14px; line-height: 18px; }
  .person__title { color: var(--text-muted); font-size: 10px; line-height: 13px; }

  .address {
    position: absolute;
    right: 238px;
    top: 195px;
    text-align: right;
    color: var(--text-light);
    font-size: 12.5px;
    line-height: 15px;
    font-style: normal;
  }
  .divider {
    position: absolute;
    left: 221px; top: 182px;
    width: 1px; height: 62px;
    background: var(--divider);
  }
  .contacts {
    position: absolute;
    left: 232px; top: 186px;
    list-style: none;
    color: var(--text-light);
    font-size: 12.5px;
    line-height: 15.5px;
  }
  .contacts li { display: flex; align-items: center; gap: 6px; }
  .contacts svg { width: 9px; height: 9px; fill: var(--brand-green); flex: none; }

  .web-band {
    position: absolute;
    left: 0; top: 249px;
    width: 100%; height: 22px;
    background: var(--brand-green);
    color: var(--text-light);
    font-size: 12.5px;
    line-height: 22px;
    text-align: center;
  }

  .tagline {
    position: absolute;
    left: 0; top: 181px;
    width: 100%;
    text-align: center;
    color: var(--brand-green);
    font-size: 16.5px;
    letter-spacing: .3px;
  }
</style>
</head>
<body>
<main class="canvas">

  <section class="card card--front" aria-label="Business card front">
    <div class="texture-area" role="img" aria-label="Faint dark machinery texture behind the card details"></div>

    <div class="brand">
      <span class="brand__square"></span>
      <span class="brand__name">
        <span class="brand__line--main">Harlow</span>
        <span class="brand__line--sub">Ironworks</span>
      </span>
    </div>

    <div class="person">
      <p class="person__name">Employee Name</p>
      <p class="person__title">Owner</p>
    </div>

    <address class="address">
      28 Anvil Street<br>
      Millbrook, NSW 2794
    </address>

    <span class="divider"></span>

    <ul class="contacts">
      <li>
        <svg viewBox="0 0 10 10" aria-hidden="true"><path d="M3 0h4a1 1 0 0 1 1 1v8a1 1 0 0 1-1 1H3a1 1 0 0 1-1-1V1a1 1 0 0 1 1-1zm0 1.5v6h4v-6z"/></svg>
        0418 539 746
      </li>
      <li>
        <svg viewBox="0 0 10 10" aria-hidden="true"><path d="M2 0l2 2.5-1 1.2c.6 1.3 1.7 2.4 3 3l1.2-1L10 8l-1.5 2C4 10 0 6 0 1.5z"/></svg>
        (02) 6193 4827
      </li>
      <li>
        <svg viewBox="0 0 10 10" aria-hidden="true"><path d="M0 2h10v6H0zm.8.6L5 5.6l4.2-3z" fill-rule="evenodd"/></svg>
        info@harlowiw.com.au
      </li>
    </ul>

    <div class="web-band">www.harlowiw.com.au</div>
  </section>

  <section class="card card--back" aria-label="Business card back">
    <div class="brand">
      <span class="brand__square"></span>
      <span class="brand__name">
        <span class="brand__line--main">Harlow</span>
        <span class="brand__line--sub">Ironworks</span>
      </span>
    </div>
    <p class="tagline">Custom Quality Fabrications</p>
  </section>

</main>
</body>
</html>
```